Plumbing business card and logo desgin

Need a new business card and logo for a plumbing business based in Warragul, Australia. Business name is 9Brook plumbing & air-conditioning. We service all plumbing and gasfitting needs and installation of air-conditioning. We clear blocked drains, install new hot water systems, central heating, new and existing homes, roofing, sanitary and drainage.
i would like to have a space on there for website, email, phone, licence number and what we do as a company.
i would like a water droplet to be incorporated into the design to try and stand out that we are a plumbing business

Contact Information for Business Card

phone number: 0497215836
Licence Number: 873614

Logo Text

9Brook Plumbing & Air-Conditioning

```html
<!DOCTYPE html>
<html lang="en">
<head>
<meta charset="utf-8">
<title>9Brook Plumbing &amp; Air-Conditioning — Business Card</title>
<link rel="stylesheet" href="https://fonts.googleapis.com/css2?family=Arimo:wght@400;700&family=Zilla+Slab:wght@700&display=swap">
<style>
  :root {
    --backdrop: #c9c9cb;
    --brand-blue: #0b8fcb;
    --brand-blue-deep: #0878ad;
    --card-white: #ffffff;
    --ink: #2b2b2b;
    --on-blue: #ffffff;
  }
  * { box-sizing: border-box; margin: 0; padding: 0; }
  html, body { width: 1200px; height: 900px; overflow: hidden; }
  body {
    background: var(--backdrop);
    font-family: "Arimo", Arial, sans-serif;
    display: flex;
    flex-direction: column;
    align-items: center;
    justify-content: center;
    gap: 56px;
  }
  .card {
    width: 640px;
    height: 366px;
    border-radius: 30px;
    position: relative;
    overflow: hidden;
    box-shadow: 0 6px 18px rgba(0,0,0,0.25);
  }

  /* Back side */
  .card--back {
    background: linear-gradient(120deg, var(--brand-blue) 55%, var(--brand-blue-deep) 100%);
    color: var(--on-blue);
    display: flex;
    flex-direction: column;
    align-items: center;
    justify-content: center;
    gap: 34px;
  }
  .brand {
    display: flex;
    align-items: center;
    gap: 12px;
    font-weight: 700;
    line-height: 1.05;
  }
  .brand__mark {
    width: 18px; height: 18px;
    border-radius: 50%;
    flex: none;
  }
  .brand__name { font-size: 46px; letter-spacing: 0.5px; }
  .brand__tag { font-size: 16px; letter-spacing: 2px; text-transform: uppercase; }
  .card--back .brand { color: var(--on-blue); }
  .card--back .brand__mark { background: var(--on-blue); }

  .services {
    list-style: none;
    text-align: center;
    font-size: 17px;
    line-height: 1.35;
  }
  .services .dot { display: inline-block; width: 7px; height: 7px; border-radius: 50%; background: var(--on-blue); margin: 0 8px; vertical-align: middle; }

  /* Front side */
  .card--front {
    background: var(--card-white);
    color: var(--ink);
    padding: 70px 0 0 72px;
  }
  .card--front .brand { color: var(--brand-blue); }
  .card--front .brand__mark { background: var(--brand-blue); }

  .person { margin-top: 34px; }
  .person__name {
    font-family: "Zilla Slab", Georgia, serif;
    font-weight: 700;
    font-size: 26px;
    color: var(--brand-blue);
    text-transform: uppercase;
    letter-spacing: 0.5px;
  }
  .person__role { font-size: 19px; margin-top: 2px; }

  .contact { list-style: none; margin-top: 18px; font-size: 18px; line-height: 1.3; }
  .contact li { display: flex; align-items: center; gap: 10px; }
  .contact svg { width: 16px; height: 16px; flex: none; fill: var(--brand-blue); }

  .licence {
    position: absolute;
    right: 40px;
    top: 150px;
    font-size: 16px;
    color: var(--ink);
  }
  .licence span { color: var(--brand-blue); }
</style>
</head>
<body>

  <section class="card card--back" aria-label="Business card, back">
    <div class="brand">
      <span class="brand__mark" aria-hidden="true"></span>
      <div>
        <div class="brand__name">9Brook</div>
        <div class="brand__tag">Plumbing &amp; Air-Conditioning</div>
      </div>
    </div>
    <ul class="services">
      <li>All plumbing<span class="dot"></span>Gasfitting<span class="dot"></span>Installation of air-conditioning</li>
      <li>Clear blocked drains<span class="dot"></span>Install new hot water systems</li>
      <li>Central Heating<span class="dot"></span>New and Existing homes</li>
      <li>Roofing<span class="dot"></span>Sanitary and Drainage</li>
    </ul>
  </section>

  <section class="card card--front" aria-label="Business card, front">
    <div class="brand">
      <span class="brand__mark" aria-hidden="true"></span>
      <div>
        <div class="brand__name">9Brook</div>
        <div class="brand__tag">Plumbing &amp; Air-Conditioning</div>
      </div>
    </div>

    <div class="person">
      <div class="person__name">Owen Hale</div>
      <div class="person__role">Managing Director</div>
    </div>

    <ul class="contact">
      <li>
        <svg viewBox="0 0 24 24" aria-hidden="true"><path d="M6.6 10.8a15.1 15.1 0 0 0 6.6 6.6l2.2-2.2a1 1 0 0 1 1-.25 11.4 11.4 0 0 0 3.6.57 1 1 0 0 1 1 1V20a1 1 0 0 1-1 1A17 17 0 0 1 3 4a1 1 0 0 1 1-1h3.5a1 1 0 0 1 1 1c0 1.25.2 2.45.57 3.6a1 1 0 0 1-.25 1z"/></svg>
        0497215836
      </li>
      <li>
        <svg viewBox="0 0 24 24" aria-hidden="true"><path d="M2 5h20v14H2z M4 7v.4l8 5 8-5V7l-8 5z" fill-rule="evenodd"/></svg>
        info@9brookplumbing.com
      </li>
      <li>
        <svg viewBox="0 0 24 24" aria-hidden="true"><path d="M12 2a10 10 0 1 0 0 20 10 10 0 0 0 0-20zm6.9 6h-2.9a15.6 15.6 0 0 0-1.4-3.6A8 8 0 0 1 18.9 8zM12 4c.8 1.2 1.5 2.5 1.9 4h-3.8c.4-1.5 1.1-2.8 1.9-4zM4.3 14a8 8 0 0 1 0-4h3.4a16 16 0 0 0 0 4zm.8 2h2.9c.3 1.3.8 2.5 1.4 3.6A8 8 0 0 1 5.1 16zM8 8H5.1a8 8 0 0 1 4.3-3.6C8.8 5.5 8.3 6.7 8 8zm4 12c-.8-1.2-1.5-2.5-1.9-4h3.8c-.4 1.5-1.1 2.8-1.9 4zm2.3-6H9.7a14 14 0 0 1 0-4h4.6a14 14 0 0 1 0 4zm.3 5.6c.6-1.1 1.1-2.3 1.4-3.6h2.9a8 8 0 0 1-4.3 3.6zm1.7-5.6a16 16 0 0 0 0-4h3.4a8 8 0 0 1 0 4z"/></svg>
        www.9brookplumbing.com
      </li>
    </ul>

    <p class="licence"><span>LIC NO:</span> 873614</p>
  </section>

</body>
</html>
```